2026 Company Line Card

We would like to redesign our current company line card. We send this printed flyer to prospective customers to introduce our company, the brands we represent, and our competitive advantages. Our website is www.valvorimsupply.com, and our phone number is (800) 312-4470. We're a specialty supplier for plumbing material, specifically water and life safety products. Our customers are mostly male, blue-collar contractors, ages 40-60. I have included a pdf of our current flyer and our high-resolution transparent logo. We would also like to highlight certain key points, which include:
Genuine OEM Parts
Technical Assistance from Repair Experts
Repair Information
1-2 day Delivery for the United States
Friendly & Knowledgeable Customer Service
The Largest Parts Inventory In The Nation
Testing Equipment
Full Service Gauge Calibration and Repair

```html
<!DOCTYPE html>
<html lang="en">
<head>
<meta charset="utf-8">
<title>Valvorim Supply – Line Card</title>
<link href="https://fonts.googleapis.com/css2?family=Roboto+Condensed:wght@400;700;800&display=swap" rel="stylesheet">
<style>
  :root {
    --navy: #0f4a99;
    --navy-deep: #0a3a7d;
    --red: #c81f2e;
    --red-deep: #8f1420;
    --band-grey: #b9c2cf;
    --paper: #ffffff;
    --stage: #ececec;
    --ink: #0f3c7d;
  }
  html, body {
    margin: 0;
    width: 1200px;
    height: 641px;
    overflow: hidden;
    background: var(--stage);
  }
  .stage {
    width: 1200px;
    height: 641px;
    display: flex;
    align-items: center;
    justify-content: center;
  }
  .line-card {
    width: 464px;
    height: 600px;
    display: block;
    box-shadow: 0 2px 8px rgba(0,0,0,.18);
    font-family: "Roboto Condensed", "Arial Narrow", sans-serif;
  }
  .headline { fill: #fff; font-weight: 800; font-size: 27px; letter-spacing: .3px; }
  .benefit { fill: #fff; font-weight: 800; font-size: 27px; letter-spacing: .3px; }
  .why-title { fill: var(--ink); font-weight: 800; font-size: 30px; }
  .feature { fill: var(--ink); font-weight: 700; font-size: 19px; }
  .brand-name { fill: var(--navy); font-weight: 700; font-size: 30px; }
  .footer-web { fill: #fff; font-weight: 700; font-size: 25px; letter-spacing: 1px; }
  .footer-call { fill: #fff; font-weight: 800; font-size: 32px; letter-spacing: .5px; }
  .star { fill: #fff; }
  .star-red { fill: var(--red); }
  .icon { fill: var(--navy); }
  .partner-badge { fill: #d3d7de; }
</style>
</head>
<body>
<main class="stage">
  <svg class="line-card" viewBox="0 0 820 1060" xmlns="http://www.w3.org/2000/svg" role="document" aria-label="Valvorim Supply line card">
    <defs>
      <linearGradient id="redField" x1="0" y1="0" x2="1" y2="1">
        <stop offset="0" stop-color="#d3283a"/>
        <stop offset="1" stop-color="var(--red-deep)"/>
      </linearGradient>
      <linearGradient id="blueField" x1="0" y1="0" x2="1" y2="1">
        <stop offset="0" stop-color="#4f78c0"/>
        <stop offset="1" stop-color="#1c4b96"/>
      </linearGradient>
      <linearGradient id="bandGrey" x1="0" y1="0" x2="1" y2="0">
        <stop offset="0" stop-color="#a7b2c2"/>
        <stop offset="1" stop-color="#dde2e9"/>
      </linearGradient>
      <linearGradient id="silverField" x1="0" y1="0" x2="1" y2="0">
        <stop offset="0" stop-color="#e4e6ea"/>
        <stop offset="1" stop-color="#f6f7f9"/>
      </linearGradient>
      <linearGradient id="photoParts" x1="0" y1="0" x2="1" y2="1">
        <stop offset="0" stop-color="#8c8478"/>
        <stop offset=".5" stop-color="#a9a59e"/>
        <stop offset="1" stop-color="#6f6e70"/>
      </linearGradient>
      <linearGradient id="photoBench" x1="0" y1="0" x2="1" y2="1">
        <stop offset="0" stop-color="#4a4436"/>
        <stop offset=".6" stop-color="#6b6a3e"/>
        <stop offset="1" stop-color="#2c2a28"/>
      </linearGradient>
      <linearGradient id="photoSpring" x1="0" y1="0" x2="1" y2="1">
        <stop offset="0" stop-color="#4f5863"/>
        <stop offset=".5" stop-color="#b9bcc0"/>
        <stop offset="1" stop-color="#8a7069"/>
      </linearGradient>
      <linearGradient id="photoBrass" x1="0" y1="0" x2="1" y2="0">
        <stop offset="0" stop-color="#c7b7a6"/>
        <stop offset=".5" stop-color="#b08a3e"/>
        <stop offset="1" stop-color="#e8e8ea"/>
      </linearGradient>
    </defs>

    <!-- paper -->
    <rect width="820" height="1060" fill="var(--paper)"/>

    <!-- header brand -->
    <g class="brand">
      <circle cx="55" cy="58" r="22" fill="var(--red)"/>
      <text class="brand-name" x="90" y="68">Valvorim Supply Company</text>
    </g>

    <!-- top parts photo -->
    <polygon role="img" aria-label="Photo of brass backflow valve parts, springs and a wrench on concrete" points="0,120 380,120 258,350 0,350" fill="url(#photoParts)"/>

    <!-- red field, top right -->
    <polygon points="820,0 820,350 612,350 805,0" fill="url(#redField)"/>
    <polygon points="818,0 822,0 624,350 612,350" fill="#fff"/>

    <!-- blue benefits panel -->
    <polygon points="460,0 810,0 612,350 262,350" fill="var(--navy)"/>
    <text class="headline" x="468" y="60">THE NATION'S LEADING</text>
    <text class="headline" x="468" y="89">SOURCE FOR:</text>

    <g class="benefit-list">
      <polygon class="star" points="420,132 425,144 438,145 428,153 431,166 420,159 409,166 412,153 402,145 415,144"/>
      <text class="benefit" x="456" y="139">GENUINE</text>
      <text class="benefit" x="456" y="168">OEM PARTS</text>

      <polygon class="star" points="382,199 387,211 400,212 390,220 393,233 382,226 371,233 374,220 364,212 377,211"/>
      <text class="benefit" x="421" y="206">REPAIR</text>
      <text class="benefit" x="421" y="235">INFORMATION</text>

      <polygon class="star" points="344,266 349,278 362,279 352,287 355,300 344,293 333,300 336,287 326,279 339,278"/>
      <text class="benefit" x="383" y="273">TECHNICAL</text>
      <text class="benefit" x="383" y="302">ASSISTANCE</text>
    </g>

    <!-- middle photo row -->
    <polygon points="0,350 250,350 148,530 0,530" fill="url(#redField)"/>
    <polygon role="img" aria-label="Photo of a technician testing gauges at a workbench with yellow hoses" points="258,350 602,350 500,530 156,530" fill="url(#photoBench)"/>
    <polygon role="img" aria-label="Photo of hands holding a stainless valve spring assembly" points="610,350 820,350 820,585 480,585" fill="url(#photoSpring)"/>

    <!-- why choose band -->
    <polygon points="0,530 500,530 470,585 0,585" fill="url(#bandGrey)"/>
    <polygon class="star-red" points="36,545 40,554 50,555 42,561 45,571 36,566 27,571 30,561 22,555 32,554"/>
    <text class="why-title" x="70" y="570">WHY CHOOSE US?</text>
    <polygon class="star-red" points="337,545 341,554 351,555 343,561 346,571 337,566 328,571 331,561 323,555 333,554"/>

    <!-- blue field right lower -->
    <polygon points="820,585 820,790 705,790" fill="url(#blueField)"/>

    <!-- feature list -->
    <g class="features">
      <!-- box icon -->
      <g class="icon" transform="translate(124,612)">
        <polygon points="18,0 36,8 18,16 0,8"/>
        <polygon points="0,11 16,19 16,36 0,28"/>
        <polygon points="20,19 36,11 36,28 20,36"/>
      </g>
      <text class="feature" x="171" y="634">1-2 Day Delivery Anywhere</text>
      <text class="feature" x="171" y="656">in The US</text>

      <!-- stacked boxes icon -->
      <g class="icon" transform="translate(448,613)">
        <rect x="10" y="0" width="14" height="12" rx="2"/>
        <rect x="0" y="14" width="14" height="12" rx="2"/>
        <rect x="20" y="14" width="14" height="12" rx="2"/>
      </g>
      <text class="feature" x="494" y="634">Largest Parts Inventory</text>
      <text class="feature" x="494" y="656">In Nation</text>

      <!-- expert icon -->
      <g class="icon" transform="translate(104,665)">
        <path d="M4,9 a8,8 0 0 1 16,0 z"/>
        <circle cx="12" cy="14" r="6"/>
        <path d="M0,32 q12,-14 24,0 z"/>
      </g>
      <text class="feature" x="137" y="691">Repair Experts On Call</text>

      <!-- gear icon -->
      <g class="icon" transform="translate(435,678)">
        <circle r="13"/>
        <circle r="6" fill="#fff"/>
        <rect x="-3" y="-19" width="6" height="38"/>
        <rect x="-19" y="-3" width="38" height="6"/>
      </g>
      <text class="feature" x="460" y="691">Testing Equipment</text>

      <!-- book icon -->
      <g class="icon" transform="translate(80,712)">
        <path d="M0,2 l11,4 v20 l-11,-4 z"/>
        <path d="M24,2 l-11,4 v20 l11,-4 z"/>
      </g>
      <text class="feature" x="116" y="727">Friendly Knowledgeable</text>
      <text class="feature" x="116" y="750">Customer Service</text>

      <!-- tools icon -->
      <g class="icon" transform="translate(413,724)">
        <rect x="-3" y="-16" width="6" height="32" rx="2" transform="rotate(45)"/>
        <rect x="-3" y="-16" width="6" height="32" rx="2" transform="rotate(-45)"/>
      </g>
      <text class="feature" x="439" y="727">Full Service Gauge Department</text>
    </g>

    <!-- lower photo and partner area -->
    <polygon points="0,790 820,790 820,975 0,975" fill="url(#silverField)"/>
    <polygon role="img" aria-label="Photo of a hand holding a brass valve seat" points="0,790 355,790 258,975 0,975" fill="url(#photoBrass)"/>

    <g class="partners" aria-label="Represented manufacturer brands">
      <rect class="partner-badge" x="408" y="822" width="58" height="30" rx="4"/>
      <rect class="partner-badge" x="484" y="826" width="60" height="22" rx="4"/>
      <rect class="partner-badge" x="565" y="822" width="60" height="30" rx="4"/>
      <rect class="partner-badge" x="642" y="828" width="70" height="18" rx="4"/>
      <rect class="partner-badge" x="722" y="826" width="70" height="22" rx="4"/>

      <rect class="partner-badge" x="400" y="870" width="66" height="20" rx="4"/>
      <rect class="partner-badge" x="480" y="870" width="70" height="20" rx="4"/>
      <rect class="partner-badge" x="578" y="864" width="36" height="32" rx="4"/>
      <rect class="partner-badge" x="643" y="870" width="66" height="20" rx="4"/>
      <rect class="partner-badge" x="722" y="870" width="72" height="20" rx="4"/>

      <rect class="partner-badge" x="400" y="913" width="66" height="20" rx="4"/>
      <rect class="partner-badge" x="484" y="910" width="60" height="26" rx="4"/>
      <rect class="partner-badge" x="566" y="911" width="62" height="24" rx="12"/>
      <rect class="partner-badge" x="640" y="911" width="68" height="24" rx="4"/>
    </g>

    <!-- footer -->
    <rect x="0" y="975" width="820" height="85" fill="url(#redField)"/>
    <polygon points="0,975 405,975 360,1060 0,1060" fill="var(--navy)"/>
    <text class="footer-web" x="32" y="1021">www.valvorimsupply.com</text>
    <text class="footer-call" x="436" y="1027">CALL US (800) 312-4470</text>
  </svg>
</main>
</body>
</html>
```